brownie sticker

i need a sticker to wrap around a clear rectangle box that will contain chocolate brownies. the sticker must be 17cm x 7 cm.
the sticker will be placed in the folowing direction.
7cm of the sticker on front of box, 3cm for each side of the box, and 4 cm on the bottom to seal the box closed.
I HAVE ATTACHED A VERY ROUGH PICTURE FOR YOU TO SEE POSITION AND DIRECTION OF STICKER.

Target Market(s)

our product will be mainly seen in upmarket grocery stores and farmers markets.

Requirements
Must have
• IT MUST CONTAIN THE FOLLOWING IN SMALL PRINT at the bottom of the sticker...
produced by marigolds bakehouse
48 kellow st
cheltenham
vic 3274
ph: 047658913
email: marigoldsbakehouse@mailbrook.net

```html
<!DOCTYPE html>
<html lang="en">
<head>
<meta charset="utf-8">
<title>Marigold's Bakehouse – Box Sticker</title>
<link rel="stylesheet" href="https://fonts.googleapis.com/css2?family=Marcellus&family=Open+Sans:wght@400&display=swap">
<style>
  :root {
    --page: #ffffff;
    --cocoa: #341308;
    --cream: #fbf0b0;
    --gold-light: #f7cf63;
    --gold: #e0a02a;
    --gold-deep: #a9661b;
    --brand-ink: #4a1a14;
    --small-ink: #3a1509;
  }
  html, body {
    margin: 0;
    padding: 0;
    width: 1200px;
    height: 900px;
    overflow: hidden;
    background: var(--page);
  }
  .canvas {
    position: relative;
    width: 1200px;
    height: 900px;
  }
  .sticker-art {
    position: absolute;
    left: 0;
    top: 0;
  }
  .brand-name {
    position: absolute;
    left: 467px;
    top: 270px;
    width: 316px;
    margin: 0;
    text-align: center;
    font-family: "Marcellus", serif;
    font-weight: 400;
    color: var(--brand-ink);
    line-height: 1;
  }
  .brand-name .brand-main {
    display: block;
    font-size: 29px;
    letter-spacing: 1.5px;
  }
  .brand-name .brand-sub {
    display: block;
    margin-top: 8px;
    font-size: 12px;
    letter-spacing: 6px;
    color: var(--brand-ink);
  }
  .producer-details {
    position: absolute;
    left: 456px;
    top: 746px;
    width: 330px;
    margin: 0;
    text-align: center;
    font-family: "Open Sans", sans-serif;
    font-style: normal;
    font-size: 10px;
    line-height: 12.6px;
    color: var(--small-ink);
  }
</style>
</head>
<body>
<main class="canvas">
  <svg class="sticker-art" width="1200" height="900" viewBox="0 0 1200 900" aria-hidden="true">
    <defs>
      <linearGradient id="ring-gold" x1="0" y1="0" x2="1" y2="1">
        <stop offset="0" stop-color="var(--gold-light)"/>
        <stop offset="0.45" stop-color="var(--gold)"/>
        <stop offset="0.7" stop-color="var(--gold-deep)"/>
        <stop offset="1" stop-color="var(--gold-light)"/>
      </linearGradient>
      <linearGradient id="crescent-gold" x1="0" y1="0" x2="1" y2="1">
        <stop offset="0" stop-color="var(--gold-light)"/>
        <stop offset="0.55" stop-color="var(--gold-deep)"/>
        <stop offset="1" stop-color="var(--gold)"/>
      </linearGradient>
      <linearGradient id="base-gold" x1="0" y1="0" x2="0" y2="1">
        <stop offset="0" stop-color="var(--gold-deep)"/>
        <stop offset="0.4" stop-color="var(--gold)"/>
        <stop offset="1" stop-color="#d9a24a"/>
      </linearGradient>
    </defs>

    <rect class="sticker-strip" x="456" y="32" width="330" height="801" fill="var(--cocoa)"/>

    <circle class="seal-ring" cx="621" cy="287" r="202" fill="url(#ring-gold)"/>
    <circle class="seal-well" cx="621" cy="287" r="185" fill="var(--cocoa)"/>
    <circle class="seal-crescent" cx="614" cy="294" r="177" fill="url(#crescent-gold)"/>
    <circle class="seal-face" cx="626" cy="283" r="164" fill="var(--cream)"/>
    <path class="seal-swoosh" d="M 522 170 Q 620 105 712 180 Q 620 122 522 170 Z" fill="var(--gold)" opacity="0.85"/>

    <path class="base-band" d="M 456 772 Q 621 670 786 772 L 786 833 L 456 833 Z" fill="url(#base-gold)"/>
    <path class="base-edge" d="M 456 772 Q 621 670 786 772" fill="none" stroke="var(--gold-light)" stroke-width="3"/>
  </svg>

  <h1 class="brand-name">
    <span class="brand-main">MARIGOLD’S</span>
    <span class="brand-sub">BAKEHOUSE</span>
  </h1>

  <address class="producer-details">
    Produced by Marigold’s Bakehouse<br>
    48 Kellow St<br>
    Larkfield<br>
    KSR 3274<br>
    Tel: 047658913<br>
    Email: marigoldsbakehouse@mailbrook.net
  </address>
</main>
</body>
</html>
```